Tallow Crest Business Card

We need a business card designed for a a company called "Tallow Crest". We offer consulting, coaching and training to business leaders and coaches (across the world) using the latest findings in neuroscience, social and emotional intelligence and positive psychology. The final design should communicate the use of brain science to create sustainable relationships.

The card should be doublesided. The logo is attached and names and titles will be provided to the successful designer. Thank you.

Industry/Entity Type

Training

```html
<!DOCTYPE html>
<html lang="en">
<head>
<meta charset="utf-8">
<title>Tallow Crest Business Card</title>
<link href="https://fonts.googleapis.com/css2?family=Marcellus&display=swap" rel="stylesheet">
<style>
  :root {
    --backdrop: #e9eaeb;
    --turquoise: #0fc4c8;
    --ink: #070b0d;
    --lime: #c6f000;
    --icon: #ffffff;
    --shadow: rgba(0, 0, 0, 0.18);
  }
  * { box-sizing: border-box; margin: 0; padding: 0; }
  html, body {
    width: 922px;
    height: 1200px;
    overflow: hidden;
    background: var(--backdrop);
  }
  .canvas {
    position: relative;
    width: 922px;
    height: 1200px;
    display: flex;
    align-items: center;
    justify-content: center;
  }
  .card {
    position: relative;
    width: 820px;
    height: 490px;
    border-radius: 8px;
    overflow: hidden;
    background: var(--turquoise);
    box-shadow: 0 12px 30px var(--shadow);
    font-family: "Marcellus", "Palatino Linotype", serif;
  }
  .card__art {
    position: absolute;
    inset: 0;
    width: 100%;
    height: 100%;
  }
  .brand {
    position: absolute;
    left: 70px;
    top: 118px;
    display: flex;
    align-items: center;
    gap: 14px;
    color: var(--lime);
    font-size: 40px;
    letter-spacing: 1px;
  }
  .brand__dot {
    width: 26px;
    height: 26px;
    border-radius: 50%;
    background: var(--lime);
  }
  .identity {
    position: absolute;
    left: 560px;
    top: 198px;
    color: var(--turquoise);
  }
  .identity__name { font-size: 27px; line-height: 1.1; }
  .identity__title { font-size: 20px; margin-left: 16px; margin-top: 4px; }
  .contact {
    position: absolute;
    left: 96px;
    top: 350px;
    list-style: none;
    color: var(--turquoise);
    font-size: 21px;
  }
  .contact__item {
    display: flex;
    align-items: center;
    gap: 18px;
    height: 29px;
  }
  .contact__icon { width: 20px; height: 20px; flex: none; }
</style>
</head>
<body>
<main class="canvas">
  <section class="card" aria-label="Tallow Crest business card">
    <svg class="card__art" viewBox="0 0 820 490" aria-hidden="true">
      <path fill="var(--lime)" d="M552 0 L820 0 L820 292 C740 330 655 352 612 420 C594 450 582 470 572 490 L0 490 L0 420 C80 292 200 262 294 232 C414 194 494 154 552 0 Z"/>
      <path fill="var(--ink)" d="M562 0 L820 0 L820 302 C744 340 664 362 624 424 C606 452 596 472 588 490 L0 490 L0 436 C84 306 204 276 304 246 C424 208 506 166 562 0 Z"/>
    </svg>

    <div class="brand">
      <span class="brand__dot"></span>
      <span class="brand__name">Tallow Crest</span>
    </div>

    <div class="identity">
      <p class="identity__name">Your Name Here</p>
      <p class="identity__title">Title</p>
    </div>

    <ul class="contact">
      <li class="contact__item">
        <svg class="contact__icon" viewBox="0 0 20 20"><path fill="var(--icon)" d="M10 2 L19 10 L16 10 L16 18 L12 18 L12 13 L8 13 L8 18 L4 18 L4 10 L1 10 Z"/></svg>
        <span>Your Address Here</span>
      </li>
      <li class="contact__item">
        <svg class="contact__icon" viewBox="0 0 20 20"><rect x="2" y="4" width="16" height="12" fill="none" stroke="var(--icon)" stroke-width="1.6"/><path d="M2 4 L10 11 L18 4" fill="none" stroke="var(--icon)" stroke-width="1.6"/></svg>
        <span>hello@tallowcrest.com</span>
      </li>
      <li class="contact__item">
        <svg class="contact__icon" viewBox="0 0 20 20"><g fill="none" stroke="var(--icon)" stroke-width="1.4"><circle cx="10" cy="10" r="8"/><ellipse cx="10" cy="10" rx="3.5" ry="8"/><path d="M2 10 H18 M3.5 6 H16.5 M3.5 14 H16.5"/></g></svg>
        <span>www.tallowcrest.com</span>
      </li>
      <li class="contact__item">
        <svg class="contact__icon" viewBox="0 0 20 20"><rect x="1" y="1" width="18" height="18" rx="3" fill="var(--icon)"/><path fill="var(--ink)" d="M6 4 L8.5 4 L9.5 7.5 L8 8.8 C8.8 10.6 9.6 11.4 11.2 12.2 L12.5 10.7 L16 11.7 L16 14 C16 15 15 16 14 16 C8.5 15.6 4.4 11.5 4 6 C4 5 5 4 6 4 Z"/></svg>
        <span>42815306</span>
      </li>
    </ul>
  </section>
</main>
</body>
</html>
```